Tri-fold Brochure Design for Banking Business

The brochure we have needs to be improved - more business like and more attractive. Logo file and brochure is attached. I would like to be able to edit the text after you get done. Your ideas and changes to text are welcome. See our website www.quillbrookadvisory.com for our theme. We can use indesign to edit the text after you complete. However, please make changes to the text we have in the design that it uploaded. Your comments and changes are welcome.

Target Market(s)

Human Resources and learning & development staff at the global investment banks - Fenwright Carrow, QTRV, etc.

Industry/Entity Type

Investment Banking

Logo Text

Quillbrook Advisory Group

Font styles to use
Serif
Sans Serif

Colors
33a6d7
0493ce
3277b5
fbf289
fdf9cf
fbee3e
0555a3
85acd3

Requirements
Must have
• Must be similar to our website www.quillbrookadvisory.com. Needs to be business-like, clean fonts, sharp design. Our logo - of course.
Nice to have
• City images - seems to be our theme.

```html
<!DOCTYPE html>
<html lang="en">
<head>
<meta charset="utf-8">
<title>Quillbrook Advisory Group – Tri-fold Brochure</title>
<link rel="stylesheet" href="https://fonts.googleapis.com/css2?family=Oswald:wght@400;500&family=Open+Sans:wght@400;600&display=swap">
<style>
  :root {
    --page-bg: #e6e7e8;
    --brand-blue: #1b6d9b;
    --brand-blue-deep: #0f5783;
    --brand-blue-light: #3277b5;
    --sky: #85acd3;
    --accent-yellow: #fbee3e;
    --url-yellow: #e3d82c;
    --ink: #16324a;
    --paper: #ffffff;
    --text-light: #e4eef6;
  }
  * { box-sizing: border-box; margin: 0; padding: 0; }
  html, body { width: 1200px; height: 2400px; overflow: hidden; }
  body {
    background: var(--page-bg);
    font-family: "Open Sans", Arial, sans-serif;
    position: relative;
  }
  .spread {
    position: absolute;
    left: 45px;
    width: 1110px;
    height: 860px;
    display: flex;
    box-shadow: 0 18px 40px rgba(0,0,0,.18);
  }
  .spread--outside { top: 250px; }
  .spread--inside { top: 1290px; }
  .panel {
    position: relative;
    width: 370px;
    height: 860px;
    overflow: hidden;
    background: var(--brand-blue);
    color: var(--text-light);
  }
  .panel + .panel { border-left: 1px solid rgba(0,0,0,.08); }
  .photo { position: absolute; left: 0; width: 100%; }
  .wave { position: absolute; left: 0; width: 370px; display: block; }
  .logo {
    position: absolute;
    display: flex;
    align-items: center;
    gap: 10px;
    font-family: "Oswald", Arial, sans-serif;
    font-weight: 500;
    font-size: 21px;
    letter-spacing: 1.5px;
    text-transform: uppercase;
    color: var(--ink);
  }
  .logo__mark { width: 16px; height: 16px; border-radius: 50%; background: var(--brand-blue); flex: none; }
  .heading {
    font-family: "Oswald", Arial, sans-serif;
    font-weight: 500;
    font-size: 19px;
    letter-spacing: .5px;
    text-transform: uppercase;
    color: #fff;
  }
  .heading::after {
    content: ""; display: block; width: 90px; height: 2px;
    background: var(--accent-yellow); margin-top: 6px;
  }
  .copy { font-size: 11.5px; line-height: 1.6; color: var(--text-light); }
  .copy p + p { margin-top: 12px; }
  .url { font-size: 14px; font-weight: 600; color: var(--url-yellow); }
  .content { position: absolute; left: 34px; right: 34px; }
  .tagline {
    font-family: "Oswald", Arial, sans-serif;
    font-weight: 400;
    font-size: 30px;
    line-height: 1.2;
    text-transform: uppercase;
    color: #fff;
  }
  .contact-list { list-style: none; font-size: 11.5px; line-height: 1.5; }
  .contact-list li + li { margin-top: 8px; }
  .contact-list strong { font-weight: 600; color: #fff; letter-spacing: .5px; }
  .service-list { list-style: none; }
  .service-list li {
    position: relative; padding-left: 24px; font-size: 11.5px; line-height: 1.55; margin-bottom: 12px;
  }
  .service-list li::before {
    content: ""; position: absolute; left: 0; top: 3px; width: 11px; height: 11px;
    border: 1.5px solid #fff;
  }
  .tick-list { list-style: none; margin: 14px 0; }
  .tick-list li {
    position: relative; padding-left: 24px; font-size: 11.5px; line-height: 1.5; margin-bottom: 9px;
  }
  .tick-list svg { position: absolute; left: 0; top: 2px; }
  .subtitle {
    position: absolute; left: 0; right: 0; top: 100px; text-align: center;
    font-family: "Oswald", Arial, sans-serif; font-weight: 500; font-size: 20px;
    text-transform: uppercase; color: var(--ink); letter-spacing: .5px;
  }
</style>
</head>
<body>

<!-- Outside of the brochure -->
<section class="spread spread--outside">

  <!-- Inside flap: About us -->
  <article class="panel panel--about">
    <div class="photo" style="top:0;height:300px;background:linear-gradient(160deg,#f4f7fa 0%,#c9d7e4 45%,#8ea9c2 100%);" role="img" aria-label="City skyline blended with a faint world map"></div>
    <svg class="wave" style="top:230px" height="90" viewBox="0 0 370 90" aria-hidden="true">
      <path d="M0 40 C120 90 250 0 370 30 L370 90 L0 90 Z" fill="var(--brand-blue)"/>
      <path d="M0 40 C120 90 250 0 370 30" fill="none" stroke="#dfe9f2" stroke-width="3"/>
    </svg>
    <div class="content" style="top:330px">
      <h2 class="heading">About Us</h2>
      <div class="copy" style="margin-top:18px">
        <p>Quillbrook Advisory Group is a dedicated training and consulting firm serving financial institutions worldwide. We design programs that build lasting capability across every level of the organisation.</p>
        <p>Our globally trusted trainers have delivered programs for leading investment banks, bringing practical market insight into every classroom and session we run.</p>
      </div>
      <p class="url" style="margin-top:40px">www.quillbrookadvisory.com</p>
    </div>
  </article>

  <!-- Back panel: Get in touch -->
  <article class="panel panel--back">
    <div class="photo" style="top:0;height:560px;background:var(--paper);"></div>
    <div class="logo" style="top:46px;left:50%;transform:translateX(-50%);white-space:nowrap;font-size:18px">
      <span class="logo__mark"></span>Quillbrook Advisory Group
    </div>
    <h3 class="subtitle">Worldwide Training Service</h3>
    <div class="photo" style="top:150px;height:440px;background:radial-gradient(ellipse at 50% 60%,#fff6e6 0%,#f6c58f 30%,#b9a7a3 60%,#8aa3ba 100%);" role="img" aria-label="Businessman looking over a city skyline at sunrise"></div>
    <svg class="wave" style="top:520px" height="100" viewBox="0 0 370 100" aria-hidden="true">
      <path d="M0 20 C110 90 260 90 370 30 L370 100 L0 100 Z" fill="var(--brand-blue)"/>
      <path d="M0 20 C110 90 260 90 370 30" fill="none" stroke="#dfe9f2" stroke-width="3"/>
    </svg>
    <div class="content" style="top:640px">
      <h2 class="heading">Get In Touch</h2>
      <ul class="contact-list" style="margin-top:16px">
        <li><strong>GLOBAL:</strong><br>global@quillbrookadvisory.com</li>
        <li><strong>ASIA:</strong><br>asia@quillbrookadvisory.com</li>
        <li><strong>UNITED STATES:</strong><br>us@quillbrookadvisory.com</li>
        <li><strong>EUROPE:</strong><br>europe@quillbrookadvisory.com</li>
      </ul>
    </div>
  </article>

  <!-- Front cover -->
  <article class="panel panel--cover">
    <div class="photo" style="top:0;height:560px;background:var(--paper);"></div>
    <div class="logo" style="top:46px;left:40px">
      <span class="logo__mark"></span>Quillbrook Advisory Group
    </div>
    <div class="photo" style="top:120px;height:450px;background:linear-gradient(180deg,#ffffff 0%,#dfe7ef 35%,#a9bccf 75%,#7f97b0 100%);" role="img" aria-label="Glass skyscrapers over a faint world map"></div>
    <svg class="wave" style="top:490px" height="110" viewBox="0 0 370 110" aria-hidden="true">
      <path d="M0 80 C110 10 240 10 370 50 L370 110 L0 110 Z" fill="var(--brand-blue)"/>
      <path d="M0 80 C110 10 240 10 370 50" fill="none" stroke="#dfe9f2" stroke-width="3"/>
    </svg>
    <div class="content" style="top:660px">
      <h1 class="tagline">Your Expert Training and Consulting Partner</h1>
      <p class="url" style="margin-top:18px">www.quillbrookadvisory.com</p>
    </div>
  </article>
</section>

<!-- Inside of the brochure -->
<section class="spread spread--inside">

  <!-- Our services -->
  <article class="panel panel--services">
    <div class="photo" style="top:0;height:350px;background:linear-gradient(150deg,#eef2f6 0%,#9fb0c4 45%,#5d7591 100%);" role="img" aria-label="Businessman with tablet blended with city towers"></div>
    <svg class="wave" style="top:280px" height="90" viewBox="0 0 370 90" aria-hidden="true">
      <path d="M0 30 C120 70 260 60 370 40 L370 90 L0 90 Z" fill="var(--brand-blue)"/>
      <path d="M0 30 C120 70 260 60 370 40" fill="none" stroke="#dfe9f2" stroke-width="3"/>
    </svg>
    <div class="content" style="top:390px">
      <h2 class="heading">Our Services</h2>
      <ul class="service-list" style="margin-top:18px">
        <li>Quillbrook Advisory Group provides best in class services for all our clients.</li>
        <li>We provide highly customized programs tailored to your specific requirements.</li>
        <li>Direct interaction between our clients, consulting trainers and client service staff ensures measurable outcomes for program participants.</li>
        <li>We facilitate learning outcomes using a blended methodology combining interactive analysis, hands-on experiential models, market simulations and a state-of-the-art learning management system.</li>
        <li>Our material databanks are continuously updated to ensure accuracy and effectiveness of our services.</li>
      </ul>
    </div>
  </article>

  <!-- Why choose us -->
  <article class="panel panel--why">
    <div class="photo" style="top:0;height:350px;background:linear-gradient(180deg,#f7f9fb 0%,#d9e3ec 50%,#b3c6d7 100%);" role="img" aria-label="Soft-focus city skyline"></div>
    <svg class="wave" style="top:280px" height="90" viewBox="0 0 370 90" aria-hidden="true">
      <path d="M0 40 C110 60 250 20 370 10 L370 90 L0 90 Z" fill="var(--brand-blue)"/>
      <path d="M0 40 C110 60 250 20 370 10" fill="none" stroke="#dfe9f2" stroke-width="3"/>
    </svg>
    <div class="content" style="top:390px">
      <h2 class="heading">Why Choose Us?</h2>
      <p class="copy" style="margin-top:18px">Quillbrook Advisory Group provides expert in-house training for your staff. We cover a wide range of topics and can readily provide customized content to match your requirements.</p>
      <ul class="tick-list">
        <li><svg width="14" height="14" viewBox="0 0 14 14" aria-hidden="true"><circle cx="7" cy="7" r="7" fill="var(--accent-yellow)"/><path d="M3.8 7.2 L6 9.3 L10.2 4.8" fill="none" stroke="var(--brand-blue-deep)" stroke-width="1.6"/></svg>Highly qualified, international pool of trainers</li>
        <li><svg width="14" height="14" viewBox="0 0 14 14" aria-hidden="true"><circle cx="7" cy="7" r="7" fill="var(--accent-yellow)"/><path d="M3.8 7.2 L6 9.3 L10.2 4.8" fill="none" stroke="var(--brand-blue-deep)" stroke-width="1.6"/></svg>Strong client relationship management and support</li>
        <li><svg width="14" height="14" viewBox="0 0 14 14" aria-hidden="true"><circle cx="7" cy="7" r="7" fill="var(--accent-yellow)"/><path d="M3.8 7.2 L6 9.3 L10.2 4.8" fill="none" stroke="var(--brand-blue-deep)" stroke-width="1.6"/></svg>Competitive pricing and flexibility</li>
        <li><svg width="14" height="14" viewBox="0 0 14 14" aria-hidden="true"><circle cx="7" cy="7" r="7" fill="var(--accent-yellow)"/><path d="M3.8 7.2 L6 9.3 L10.2 4.8" fill="none" stroke="var(--brand-blue-deep)" stroke-width="1.6"/></svg>Outcome-driven approach directly matches your company's needs</li>
      </ul>
      <p class="copy">Our Consulting Trainers are sourced globally and recognized by the industry as highly effective trainers and program facilitators.</p>
    </div>
  </article>

  <!-- Our team -->
  <article class="panel panel--team">
    <div class="content" style="top:60px">
      <h2 class="heading">Our Team</h2>
      <div class="copy" style="margin-top:18px">
        <p>Our Consulting Trainers are recruited globally and recognized by the industry as highly effective trainers and program facilitators.</p>
        <p>Quillbrook Advisory Group draws on expertise from top programs with local talent for program facilitation.</p>
        <p>Our large array of Consulting Trainers lets us provide global expertise for your programs while using local talent where needed.</p>
      </div>
      <p class="url" style="margin-top:22px">www.quillbrookadvisory.com</p>
    </div>
    <div class="photo" style="top:480px;height:380px;background:linear-gradient(160deg,#f2f5f8 0%,#c8d4df 50%,#8fa6bc 100%);" role="img" aria-label="Hands working on a laptop at a meeting table"></div>
    <svg class="wave" style="top:440px" height="90" viewBox="0 0 370 90" aria-hidden="true">
      <path d="M0 0 L370 0 L370 30 C250 80 120 80 0 50 Z" fill="var(--brand-blue)"/>
      <path d="M370 30 C250 80 120 80 0 50" fill="none" stroke="#dfe9f2" stroke-width="3"/>
    </svg>
  </article>
</section>

</body>
</html>
```